Bandbanner für Melodic Metal Band
Zielgruppe
Copper Lantern ist eine Melodic Metal Band.
Wir brauchen ein neues Design für Backdrops (Bandbanner) die wir in verschiedenen Grössen drucken könnten.
(Bisher hatten wir die Grössen 500 cm x 300 cm, 400 cm x 250 cm und 200 cm x 200 cm)
Unser Bandlogo soll modern und inspiriert rüberkommen, um unsere Musik und Show zusätzlich zu unterstreichen.
Aufgabenstellung
- das Bandlogo soll stylisch und cool präsentiert sein (z.B. mit zusätzlichen Elementen ergänzt, umspielt, umrahmt... )
- einzigartig, Blickfang, auf uns zugeschnitten
- Das Design soll neu und neutral sein. Also nicht direkt bezogen auf eines unserer Alben. Wir möchten es für verschiedene Zwecke und für längere Zeit benutzen können
- modern, cool, vielleicht frech, kann Farben enthalten, hell/dunkel, mystisch
- soll zu unserem ganzen Auftreten und Style passen
- unsere Musik und Inhalte sind melodiös, modern, mal hart, mal sanfter, mal etwas dunkler, anklagend oder nachdenklich aber immer mit einer Prise Helligkeit und Hoffnung, nicht destruktiv. Deshalb nicht zu morbide oder zu klischeehaft, aber es darf gerne mysteriös oder melancholisch oder auch schlicht und speziell sein
(Das Logo und Sign könnten wir übrigens als AI, CDR, EPS, JPG, PDF, PNG und PSD zur Verfügung stellen).

```html
<!DOCTYPE html>
<html lang="de">
<head>
<meta charset="utf-8">
<title>Copper Lantern – Bandbanner</title>
<link rel="stylesheet" href="https://fonts.googleapis.com/css2?family=Open+Sans:wght@400;800&display=swap">
<style>
  :root {
    --page-bg: #ececec;
    --banner-black: #030506;
    --smoke-teal: #2fb3b8;
    --smoke-deep: #0c4f56;
    --logo-ice: #cfe6ec;
    --text-light: #e8eef0;
  }
  * { margin: 0; padding: 0; box-sizing: border-box; }
  html, body {
    width: 1200px; height: 1200px; overflow: hidden;
    background: var(--page-bg);
    font-family: "Open Sans", Arial, sans-serif;
  }
  .banner {
    position: absolute; left: 30px; top: 258px;
    width: 1140px; height: 684px;
    background: var(--banner-black);
    overflow: hidden;
  }
  .banner__smoke {
    position: absolute; inset: 0;
    background:
      radial-gradient(ellipse 220px 260px at 60px 420px, rgba(47,179,184,.55), transparent 70%),
      radial-gradient(ellipse 200px 160px at 720px 150px, rgba(47,179,184,.45), transparent 70%),
      radial-gradient(ellipse 180px 200px at 1050px 140px, rgba(47,179,184,.5), transparent 70%),
      radial-gradient(ellipse 260px 200px at 880px 480px, rgba(47,179,184,.35), transparent 70%),
      radial-gradient(ellipse 300px 180px at 420px 470px, rgba(12,79,86,.7), transparent 70%),
      radial-gradient(ellipse 240px 160px at 150px 640px, rgba(47,179,184,.4), transparent 70%),
      radial-gradient(ellipse 260px 180px at 1040px 640px, rgba(47,179,184,.35), transparent 70%);
  }
  .members {
    position: absolute; top: 60px; left: 0; right: 0;
    list-style: none;
    color: var(--text-light);
    font-size: 12px; font-weight: 400; letter-spacing: .04em;
    text-transform: uppercase;
  }
  .members li { position: absolute; white-space: nowrap; }
  .members li:nth-child(1) { left: 144px; }
  .members li:nth-child(2) { left: 406px; top: 22px; }
  .members li:nth-child(3) { left: 690px; top: 34px; }
  .members li:nth-child(4) { left: 900px; top: 40px; }
  .band-name {
    position: absolute; left: 0; right: 0; top: 300px;
    text-align: center;
    color: var(--logo-ice);
    font-weight: 800; font-size: 108px; line-height: 1;
    letter-spacing: .02em; text-transform: uppercase;
  }
  .tagline {
    position: absolute; left: 0; right: 0; top: 620px;
    text-align: center;
    color: var(--text-light);
    font-size: 12px; line-height: 1.45;
  }
</style>
</head>
<body>
  <section class="banner">
    <div class="banner__smoke" role="img" aria-label="Türkisfarbene Rauchschwaden auf schwarzem Grund"></div>
    <ul class="members">
      <li>Saskia Brenner</li>
      <li>Tobias Lendl</li>
      <li>Jonas Vogt</li>
      <li>Marco Keller</li>
    </ul>
    <h1 class="band-name">Copper Lantern</h1>
    <p class="tagline">Lorem ipsum dolor sit amet, consectetur adipiscing elit,<br>sed do eiusmod tempor incididunt ut labore et dolore<br>magna aliqua. Quis ipsum suspendisse ultrices gravida. sis.</p>
  </section>
</body>
</html>
```